Christmas Collection Candle Label Design

Looking to update our existing Christmas Candle Collection labels. Labels should reflect the overall feel of our brand- www.wickmerelane.ca
Want to include some color elements. Holiday colors added into design but more muted/ earthy tones not vibrant colors . Metallic elements and line art botanical illustration. Fonts should be more align to brand
Scents
Holiday Tree
Candy Cane
Sugar and Spice
Joyeaux Noel

```html
<!DOCTYPE html>
<html lang="en">
<head>
<meta charset="utf-8">
<title>Holiday Tree – Candle Label</title>
<link rel="stylesheet" href="https://fonts.googleapis.com/css2?family=Playfair+Display:wght@400;500&family=Great+Vibes&family=Montserrat:wght@400;500&family=Libre+Caslon+Text&display=swap">
<style>
  :root {
    --label-bg: #f4f5f5;
    --ink: #1e1c1a;
    --ink-soft: #2b2a2e;
    --sketch: #8a7a68;
    --sketch-light: #c7bcaf;
    --band-start: #6e6152;
    --band-end: #2f2a25;
    --band-text: #f6f2ec;
  }
  * { margin: 0; padding: 0; box-sizing: border-box; }
  html, body {
    width: 1200px; height: 1200px; overflow: hidden;
    background: var(--label-bg);
  }
  .label {
    position: relative; width: 1200px; height: 1200px;
    background: radial-gradient(circle at 70% 40%, #fafbfb 0%, var(--label-bg) 70%);
    color: var(--ink);
  }
  .botanical { position: absolute; }
  .botanical--pine-top-left {
    left: 0; top: 0; width: 280px; height: 330px;
    background: radial-gradient(ellipse at 20% 40%, var(--sketch-light) 0%, rgba(199,188,175,0.25) 65%, transparent 100%);
  }
  .botanical--cone-top-right {
    right: 0; top: 0; width: 210px; height: 240px;
    background: radial-gradient(ellipse at 60% 35%, var(--sketch-light) 0%, rgba(199,188,175,0.25) 65%, transparent 100%);
  }
  .botanical--cone-bottom-left {
    left: 0; top: 670px; width: 385px; height: 407px;
    background: radial-gradient(ellipse at 35% 50%, var(--sketch-light) 0%, rgba(199,188,175,0.25) 65%, transparent 100%);
  }
  .botanical--cone-bottom-right {
    right: 0; top: 890px; width: 150px; height: 187px;
    background: radial-gradient(ellipse at 60% 50%, var(--sketch-light) 0%, rgba(199,188,175,0.25) 65%, transparent 100%);
  }
  .brand {
    position: absolute; top: 120px; left: 0; width: 1200px;
    text-align: center;
  }
  .brand__name {
    font-family: "Playfair Display", serif;
    font-weight: 400; font-size: 50px; letter-spacing: 1px;
    color: var(--ink); line-height: 1;
  }
  .brand__tagline {
    margin-top: 10px;
    font-family: "Montserrat", sans-serif; font-weight: 500;
    font-size: 13px; letter-spacing: 3px; color: var(--ink-soft);
  }
  .claim {
    position: absolute; top: 290px; left: 0; width: 1200px; text-align: center;
    font-family: "Montserrat", sans-serif; font-size: 35px; font-weight: 400;
    color: var(--ink-soft);
  }
  .scent-name {
    position: absolute; top: 380px; left: 0; width: 1200px; text-align: center;
    font-family: "Playfair Display", serif; font-weight: 500;
    font-size: 200px; line-height: 1; letter-spacing: -2px; color: var(--ink);
  }
  .scent-name__script {
    position: absolute; top: 560px; left: 630px;
    font-family: "Great Vibes", cursive;
    font-size: 250px; line-height: 1; color: var(--ink);
  }
  .notes {
    position: absolute; top: 815px; left: 0; width: 1200px; text-align: center;
    font-family: "Libre Caslon Text", serif; font-size: 38px; color: var(--ink);
    padding-left: 0;
  }
  .details {
    position: absolute; top: 1077px; left: 0; width: 1200px; height: 84px;
  }
  .details__item {
    position: absolute; top: 0; height: 84px;
    display: flex; align-items: center; justify-content: center;
    background: linear-gradient(90deg, var(--band-start), var(--band-end));
    font-family: "Libre Caslon Text", serif; font-size: 28px; color: var(--band-text);
  }
  .details__item--weight { left: 0; width: 390px; }
  .details__item--origin { left: 403px; width: 397px; }
  .details__item--wax { left: 811px; width: 389px; }
</style>
</head>
<body>
  <main class="label">
    <div class="botanical botanical--pine-top-left" role="img" aria-label="Line-art pine branch illustration"></div>
    <div class="botanical botanical--cone-top-right" role="img" aria-label="Line-art pine cone illustration"></div>
    <div class="botanical botanical--cone-bottom-left" role="img" aria-label="Line-art pine cone with fir branch illustration"></div>
    <div class="botanical botanical--cone-bottom-right" role="img" aria-label="Line-art small pine cone illustration"></div>

    <header class="brand">
      <div class="brand__name">WICKMERE LANE</div>
      <div class="brand__tagline">PURE PLANT BASED SCENTS</div>
    </header>

    <p class="claim">Made with Plant Based Botanicals</p>

    <h1 class="scent-name">HOLIDAY</h1>
    <div class="scent-name__script">tree</div>

    <p class="notes">Peppercorn - Ginger - Lemon Peel</p>

    <footer class="details">
      <div class="details__item details__item--weight">Net Wt 100g</div>
      <div class="details__item details__item--origin">Made in Canada</div>
      <div class="details__item details__item--wax">Natural Soy</div>
    </footer>
  </main>
</body>
</html>
```